Fresh, modern, fun business card for pediatric dental practice

Need a business card for fresh, modern, fun pediatric dental practice

Clean look that matches our website's font and colors

We prefer the look of curved corners on business cards

Target Market(s)

parents (mothers) of young children, professionals, mid-high class

Industry/Entity Type

Dental

Contact Information for Business Card

Maplewood Pediatric Dentistry
482 Corbett Lane
Suite 619
Fernhollow, PA 17599
717.555.0193
www.maplewoodtotsdental.example

Mei-Hua Tran, DMD
Colette Margrave, DMD
(we are working on our email address, but we would like that on the card as well)

Font styles to use
Sans Serif

Requirements
Must have
• All info; we would also like to make cards for individual staff members
• colors from our website and color palatte, attatched
• use same font and design as website for branding
Nice to have
• clean, simple card that has a pop of color
• we would like to see a few designs with our tag line "where smiles get brighter"
• we are not sure if we want to have it on there or not
• we would like to see a few designs incorporating the ribbon graphic on our website where the word WELCOME is

```html
<!DOCTYPE html>
<html lang="en">
<head>
<meta charset="utf-8">
<title>Maplewood Pediatric Dentistry – Business Card</title>
<link rel="stylesheet" href="https://fonts.googleapis.com/css2?family=Lato:wght@400;700;900&display=swap">
<style>
  :root {
    --page-bg: #1c1c1c;
    --card-bg: #262626;
    --card-bg-light: #2e2e2e;
    --sun-yellow: #f6b91c;
    --berry-pink: #c8348f;
    --ink-white: #f1f1f1;
    --emboss-grey: #6a6a6a;
  }
  * { box-sizing: border-box; margin: 0; padding: 0; }
  html, body {
    width: 1200px; height: 900px; overflow: hidden;
    background: var(--page-bg);
    font-family: "Lato", sans-serif;
  }
  .sheet {
    width: 1200px; height: 900px;
    display: flex; flex-direction: column; align-items: center; justify-content: center;
    gap: 44px;
  }
  .card {
    position: relative;
    width: 680px; height: 388px;
    background: linear-gradient(135deg, var(--card-bg-light), var(--card-bg));
    box-shadow: 0 18px 40px rgba(0,0,0,.55);
    overflow: hidden;
  }
  .card::after {
    content: ""; position: absolute; left: 0; right: 0; bottom: 0;
    height: 8px; background: var(--sun-yellow);
  }

  /* Front */
  .card-front { display: flex; flex-direction: column; align-items: center; justify-content: center; }
  .brand-front { display: flex; align-items: center; gap: 18px; margin-top: -10px; }
  .brand-dot { width: 30px; height: 30px; border-radius: 50%; flex: none; }
  .brand-front .brand-dot { background: var(--emboss-grey); }
  .brand-name { font-weight: 900; line-height: 1.05; letter-spacing: 1px; }
  .brand-front .brand-name { color: var(--emboss-grey); font-size: 44px; }
  .front-web {
    position: absolute; bottom: 36px; left: 0; right: 0; text-align: center;
    font-size: 17px; letter-spacing: 2px; color: var(--ink-white);
  }
  .front-web .domain { color: var(--sun-yellow); }

  /* Back */
  .card-back { display: flex; align-items: center; padding: 0 30px 0 36px; }
  .brand-back { width: 270px; display: flex; flex-direction: column; align-items: center; gap: 14px; flex: none; }
  .brand-back .brand-dot { background: var(--sun-yellow); }
  .brand-back .brand-name { color: var(--sun-yellow); font-size: 34px; text-align: center; }
  .divider { width: 3px; height: 210px; background: var(--berry-pink); margin: 0 30px 0 24px; flex: none; }
  .contact { color: var(--ink-white); font-size: 17px; line-height: 1.3; }
  .person-name { color: var(--sun-yellow); font-weight: 700; font-size: 25px; letter-spacing: 1.5px; text-transform: uppercase; }
  .person-title { font-size: 18px; margin-bottom: 14px; }
  .practice { color: var(--sun-yellow); }
  .address { margin-bottom: 12px; }
  .contact-list { list-style: none; }
  .contact-list li { display: flex; align-items: center; gap: 12px; letter-spacing: .3px; white-space: nowrap; }
  .contact-list svg { width: 15px; height: 15px; flex: none; fill: var(--sun-yellow); }
</style>
</head>
<body>
<main class="sheet">
  <section class="card card-front">
    <div class="brand-front">
      <span class="brand-dot"></span>
      <div class="brand-name">Maplewood<br>Pediatric Dentistry</div>
    </div>
    <p class="front-web">www.<span class="domain">maplewoodtotsdental</span>.example</p>
  </section>

  <section class="card card-back">
    <div class="brand-back">
      <span class="brand-dot"></span>
      <div class="brand-name">Maplewood<br>Pediatric<br>Dentistry</div>
    </div>
    <div class="divider"></div>
    <div class="contact">
      <p class="person-name">Colette Margrave</p>
      <p class="person-title">DMD</p>
      <p class="practice">Maplewood Pediatric Dentistry</p>
      <p class="address">482 Corbett Lane<br>Suite 619 Fernhollow, PA 17599</p>
      <ul class="contact-list">
        <li><svg viewBox="0 0 24 24" aria-hidden="true"><path d="M6.6 10.8a15 15 0 0 0 6.6 6.6l2.2-2.2a1 1 0 0 1 1-.25 11.4 11.4 0 0 0 3.6.57 1 1 0 0 1 1 1V20a1 1 0 0 1-1 1A17 17 0 0 1 3 4a1 1 0 0 1 1-1h3.5a1 1 0 0 1 1 1c0 1.25.2 2.45.57 3.57a1 1 0 0 1-.25 1z"/></svg>717.555.0193</li>
        <li><svg viewBox="0 0 24 24" aria-hidden="true"><path d="M2 5h20v14H2zm2 2v.5l8 5 8-5V7l-8 5z"/></svg>info@maplewoodtotsdental.example</li>
        <li><svg viewBox="0 0 24 24" aria-hidden="true"><path d="M12 2a10 10 0 1 0 0 20 10 10 0 0 0 0-20zm6.9 6h-3a15 15 0 0 0-1.3-3.9A8 8 0 0 1 18.9 8zM12 4c.8 1.1 1.5 2.5 1.9 4h-3.8c.4-1.5 1.1-2.9 1.9-4zM4.3 14a8 8 0 0 1 0-4h3.4a16 16 0 0 0 0 4zm.8 2h3a15 15 0 0 0 1.3 3.9A8 8 0 0 1 5.1 16zm3-8h-3a8 8 0 0 1 4.3-3.9A15 15 0 0 0 8.1 8zM12 20c-.8-1.1-1.5-2.5-1.9-4h3.8c-.4 1.5-1.1 2.9-1.9 4zm2.3-6H9.7a14 14 0 0 1 0-4h4.6a14 14 0 0 1 0 4zm.3 5.9a15 15 0 0 0 1.3-3.9h3a8 8 0 0 1-4.3 3.9zm1.7-5.9a16 16 0 0 0 0-4h3.4a8 8 0 0 1 0 4z"/></svg>www.maplewoodtotsdental.example</li>
      </ul>
    </div>
  </section>
</main>
</body>
</html>
```